Asia based real estate financing firm needs and AWESOME design for a biz card -Harborline Lending Partners

Looking for a stylish, & corporate-looking business card for a real estate financing brokerage firm in Asia, offering global mortgage loans. I uploaded our current logos. We would like to add a splash of color (perhaps the house icon) or any other suggestions are open. For the winning designer, we have a lot of work! Thanks and best of luck!

Target Market(s)

Real estate investors globally. We want to look more like a BANK and NOT a real estate company. Please don't play up on a "house" design.

Industry/Entity Type

Banking

Contact Information for Business Card

Harborline Lending Partners
Peter Walsh
Co-Founder | Partner

42 Kelvin Street, Suite 310
Singapore 074219
www.hlp-lend.example
peterwalsh@hlp-lend.example
+65 555-0147
WeChat: peterwalsh

Colors

Designer to choose colors to be used in the design.

Requirements
Must have
• Must have the standard business requirements for a card; name, address, email, etc
• Can be horizontal or vertical.
Nice to have
• It would be great to see some sort of variation to the logo with a pop of color. Red is good as we're in Asia, however, other options work as well.
• Our tag line is - Borderless mortgages. It doesn't have to be on the card but might be nice.
• I'd like to start seeing our tagline within the cards as well. - Borderless mortgages.
• Also, please add our location. The location for this card is Singapore so perhaps it can be highlighted or emphasised in some way.
• Singapore | Hong Kong | Shanghai | Manila
• As we will soon open an office in Shanghai, having an option for both languages would be great.
Should not have
• I'm exceited and open to your creativity ... knock it out of the park!

```html
<!DOCTYPE html>
<html lang="en">
<head>
<meta charset="utf-8">
<title>Harborline Lending Partners – Business Card</title>
<link rel="stylesheet" href="https://fonts.googleapis.com/css2?family=Work+Sans:wght@400;500;600&display=swap">
<style>
  :root {
    --backdrop: #a9a9a9;
    --brand-blue: #2561ae;
    --card-white: #ffffff;
    --ink: #1c1c1c;
    --on-blue: #ffffff;
  }
  * { box-sizing: border-box; margin: 0; padding: 0; }
  html, body { width: 1200px; height: 930px; overflow: hidden; }
  body {
    background: var(--backdrop);
    font-family: "Work Sans", Arial, sans-serif;
    position: relative;
  }
  .card {
    position: absolute;
    width: 540px;
    height: 310px;
    border-radius: 18px;
    box-shadow: 0 6px 14px rgba(0,0,0,0.25);
    overflow: hidden;
  }
  .card-front {
    left: 110px; top: 140px;
    background: var(--brand-blue);
    color: var(--on-blue);
    display: flex; flex-direction: column; align-items: center; justify-content: center;
    text-align: center;
  }
  .company-name {
    font-size: 30px; font-weight: 500; letter-spacing: 1px; line-height: 1.25;
    width: 360px;
  }
  .tagline {
    margin-top: 40px;
    font-size: 14px; font-weight: 400; letter-spacing: 1.5px; text-transform: uppercase;
  }
  .card-back {
    left: 550px; top: 480px;
    background: var(--card-white);
    color: var(--ink);
  }
  .holder {
    position: absolute; right: 284px; top: 118px; text-align: left;
  }
  .holder-name {
    font-size: 25px; font-weight: 600; color: var(--brand-blue); letter-spacing: 0.5px;
    text-transform: uppercase; line-height: 1.1; white-space: nowrap;
  }
  .holder-title { font-size: 14px; margin-top: 4px; white-space: nowrap; }
  .divider {
    position: absolute; left: 272px; top: 84px; width: 1.5px; height: 104px;
    background: var(--brand-blue);
  }
  .contact-list {
    position: absolute; left: 288px; top: 86px; list-style: none;
    font-size: 13px; line-height: 25px;
  }
  .contact-list li { display: flex; align-items: center; gap: 7px; white-space: nowrap; }
  .contact-list svg { width: 11px; height: 11px; flex: none; }
  .address {
    position: absolute; right: 30px; bottom: 40px; font-size: 14px; letter-spacing: 0.3px;
    white-space: nowrap;
  }
</style>
</head>
<body>
  <section class="card card-front">
    <h1 class="company-name">Harborline Lending Partners</h1>
    <p class="tagline">Borderless Mortgages</p>
  </section>

  <section class="card card-back">
    <div class="holder">
      <h2 class="holder-name">Peter Walsh</h2>
      <p class="holder-title">Co-Founder | Partner</p>
    </div>
    <div class="divider"></div>
    <ul class="contact-list">
      <li><svg viewBox="0 0 12 12" aria-hidden="true"><path d="M2 1 L4 1 L5 3.5 L3.8 4.5 Q5 7 7.5 8.2 L8.5 7 L11 8 L11 10 Q10.5 11 9 11 Q1 9 1 2 Q1.5 1 2 1Z" fill="#2561ae"/></svg>+65 555-0147</li>
      <li><svg viewBox="0 0 12 12" aria-hidden="true"><rect x="1" y="2.5" width="10" height="7" fill="none" stroke="#2561ae" stroke-width="1.3"/><path d="M1 2.5 L6 6.5 L11 2.5" fill="none" stroke="#2561ae" stroke-width="1.3"/></svg>peterwalsh@hlp-lend.example</li>
      <li><svg viewBox="0 0 12 12" aria-hidden="true"><circle cx="6" cy="6" r="5" fill="none" stroke="#2561ae" stroke-width="1.2"/><ellipse cx="6" cy="6" rx="2.2" ry="5" fill="none" stroke="#2561ae" stroke-width="1"/><path d="M1 6 H11" stroke="#2561ae" stroke-width="1"/></svg>www.hlp-lend.example</li>
      <li><svg viewBox="0 0 12 12" aria-hidden="true"><circle cx="6" cy="6" r="5" fill="#2561ae"/></svg>peterwalsh</li>
    </ul>
    <p class="address">42 Kelvin Street, Suite 310 Singapore 074219</p>
  </section>
</body>
</html>
```